Criação de Papelaria (6 itens) para Brisa & Lajedo
" Prestamos serviços de outorga e licenças ambientais, análise de água, aproveitamento de águas, pesquisa de água mineral, poços artesianos (furação, recuperação, tratamento de água), energia solar, etc. "

```html
<!DOCTYPE html>
<html lang="pt-BR">
<head>
<meta charset="UTF-8">
<title>Brisa &amp; Lajedo — Envelope</title>
<link rel="stylesheet" href="https://fonts.googleapis.com/css2?family=Montserrat:wght@400;500;600&display=swap">
<style>
  :root {
    --backdrop: #b9babd;
    --paper: #ffffff;
    --brand-blue: #2f5596;
    --brand-green: #6d9a3a;
    --ink: #2a2a2a;
    --fold-line: #e3e4e6;
  }
  * { margin: 0; padding: 0; box-sizing: border-box; }
  html, body { width: 1200px; height: 1200px; overflow: hidden; }
  body {
    background: var(--backdrop);
    font-family: "Montserrat", Arial, sans-serif;
    position: relative;
  }
  .envelope {
    position: absolute;
    left: 240px;
    width: 720px;
    height: 408px;
    background: var(--paper);
    overflow: hidden;
  }
  .envelope--front { top: 168px; }
  .envelope--back { top: 636px; }
  .flap-line { position: absolute; inset: 0; width: 100%; height: 100%; }
  .envelope__band {
    position: absolute;
    left: 0; right: 0; bottom: 14px;
    height: 15px;
    background: var(--brand-blue);
  }
  .brand {
    position: absolute;
    left: 0; right: 0;
    text-align: center;
    color: var(--brand-blue);
  }
  .brand__name { font-weight: 600; display: block; letter-spacing: 0.5px; }
  .brand__tagline {
    display: block;
    font-weight: 500;
    text-transform: uppercase;
  }
  .envelope--front .brand { top: 178px; }
  .envelope--front .brand__name { font-size: 50px; line-height: 1; }
  .envelope--front .brand__tagline { font-size: 20px; letter-spacing: 2.4px; margin-top: 12px; }
  .envelope--back .brand { top: 266px; }
  .envelope--back .brand__name { font-size: 22px; line-height: 1; }
  .envelope--back .brand__tagline { font-size: 8px; letter-spacing: 1px; margin-top: 3px; }
  .contact {
    position: absolute;
    left: 0; right: 0; top: 314px;
    text-align: center;
    color: var(--ink);
    font-size: 13px;
    line-height: 15px;
  }
  .contact__row span { display: inline-block; width: 180px; }
</style>
</head>
<body>
  <section class="envelope envelope--front">
    <svg class="flap-line" viewBox="0 0 720 408" aria-hidden="true">
      <polyline points="0,0 360,62 720,0" fill="none" stroke="var(--fold-line)" stroke-width="2"/>
    </svg>
    <div class="brand">
      <span class="brand__name">Brisa &amp; Lajedo</span>
      <span class="brand__tagline">Soluções Ambientais</span>
    </div>
    <div class="envelope__band"></div>
  </section>

  <section class="envelope envelope--back">
    <div class="brand">
      <span class="brand__name">Brisa &amp; Lajedo</span>
      <span class="brand__tagline">Soluções Ambientais</span>
    </div>
    <address class="contact" style="font-style:normal">
      <div class="contact__row"><span>(00) 0000-0000</span><span>(00) 00000-0000</span></div>
      <div class="contact__row"><span>www.brisalajedo.com.br</span><span>contato@brisalajedo.com.br</span></div>
      <div>Rua das Palmeiras nº120 - Vila Aurora - São Paulo - SP - 01234-000</div>
    </address>
    <div class="envelope__band"></div>
  </section>
</body>
</html>
```